HK-Steuerberatung WordPress Site fully implemented (tax advisor)

Hello!
I need a little Wordpress Site for my newly founded Tax-Advisor Company.
I am a one-man Office advising in the area of Crypto-Currency.
PLEASE only provide a Design, if you can also Implement a WP-Site afterwards on an existing Webspace.

Please find the Content and Website-Description in the attached Document

Language for the Website is German (for now)

Target Market(s)

Tax-Advisory (specialized in Crypto Currency)

Coding

Coded - Design and coding required

Number of Pages Required

5+ page

Font styles to use
Sans Serif

Requirements
Must have
• Wordpress Implementation afterwards - Details according to attached Project Information Document

```html
<!DOCTYPE html>
<html lang="de">
<head>
<meta charset="utf-8">
<title>HK-Steuerberatung</title>
<link rel="stylesheet" href="https://fonts.googleapis.com/css2?family=Poppins:wght@400;500;600;700;800&family=Hind:wght@400;500&display=swap">
<style>
:root{
  --navy:#0f2540;
  --orange:#f96a0b;
  --orange-dark:#f0520a;
  --text:#5b6470;
  --muted:#9aa3ad;
  --line:#e9ecef;
  --white:#ffffff;
}
*{box-sizing:border-box;margin:0;padding:0}
html,body{width:1200px;height:4399px;overflow:hidden}
body{position:relative;background:var(--white);font-family:"Hind",sans-serif;color:var(--text);font-size:14px;line-height:1.9}
.abs{position:absolute}
h1,h2,h3,h4{font-family:"Poppins",sans-serif;color:var(--navy)}
.btn{position:absolute;display:flex;align-items:center;justify-content:center;background:var(--orange);color:var(--white);font-family:"Poppins",sans-serif;font-weight:700;font-size:16px}

/* hero */
.hero{left:0;top:0;width:1200px;height:862px;background:linear-gradient(120deg,#f3f6f6 0%,#eef2f3 40%,#f4f0ee 70%,#f1f4f0 100%)}
.hero-glow{left:0;top:0;width:1200px;height:140px;background:linear-gradient(90deg,rgba(255,240,215,.6),rgba(230,245,235,.6) 40%,rgba(240,230,250,.6) 75%,rgba(235,245,255,.5))}
.nav{top:24px;left:99px;width:1002px;height:20px;display:flex;align-items:center;font-family:"Poppins",sans-serif;font-size:12px;font-weight:500;color:var(--navy)}
.nav-links{display:flex;gap:30px}
.nav-links span::after{content:" ⌄";font-size:10px}
.brand{position:absolute;left:410px;top:-6px;display:flex;align-items:center;gap:8px;font-weight:600;font-size:12px;letter-spacing:.3px}
.brand i{display:block;width:20px;height:24px;background:var(--navy)}
.nav-contact{position:absolute;right:0;display:flex;gap:26px;font-size:12px}
.hero h1{left:99px;top:160px;font-size:60px;font-weight:800;line-height:1.13;letter-spacing:-.5px;white-space:nowrap}
.hero-lead{left:99px;top:382px;width:380px;font-size:14px;line-height:2}
.hero .btn{left:99px;top:480px;width:198px;height:56px}
.stats{left:99px;top:608px;display:flex;gap:62px}
.stat b{display:block;font-family:"Poppins",sans-serif;font-size:38px;font-weight:700;color:var(--navy);line-height:1.2}
.stat span{display:block;font-family:"Poppins",sans-serif;font-size:14px;color:var(--navy);line-height:1.55;margin-top:6px}
.hero-photo{left:589px;top:188px;width:571px;height:674px;background:linear-gradient(180deg,#dfe1e3 0%,#c7cacd 50%,#b8b1a8 100%);border-radius:240px 240px 0 0}
.stat-card{left:662px;top:193px;width:171px;height:111px;background:var(--white);border-radius:10px;box-shadow:0 10px 30px rgba(15,37,64,.1);padding:16px 18px;font-size:10px;line-height:1.4}
.stat-card .row{display:flex;justify-content:space-between}
.stat-card .vals{margin-top:16px;font-family:"Poppins",sans-serif;font-weight:600;font-size:13px;color:var(--navy)}
.stat-card .vals em{font-style:normal;color:var(--orange)}
.stat-card .bar{margin-top:10px;height:6px;background:#eef0f2;border-radius:3px}
.stat-card .bar i{display:block;width:35%;height:100%;background:var(--orange);border-radius:3px}
.side-tools{left:1160px;top:196px;width:40px;height:188px;background:var(--white);box-shadow:0 4px 20px rgba(0,0,0,.08);display:flex;flex-direction:column;align-items:center;justify-content:space-around;padding:8px 0}
.side-tools i{display:block;width:14px;height:14px;border:1.6px solid var(--navy);border-radius:3px}

/* feature cards */
.feature{top:809px;width:321px;height:297px;background:var(--white);box-shadow:0 14px 34px rgba(15,37,64,.07);padding:12px 0 0 36px}
.feature::after{content:"";position:absolute;left:8px;right:8px;bottom:0;height:4px;background:var(--orange)}
.feature .num{font-family:"Poppins",sans-serif;font-size:22px;color:#c8cdd2;margin-left:-26px}
.feature h3{margin-top:20px;font-size:28px;font-weight:600;line-height:1.3}
.feature p{margin-top:36px;width:250px;font-size:14px;line-height:2}

/* benefits */
.pillar{left:99px;width:186px;height:155px;background:var(--white);box-shadow:0 14px 34px rgba(15,37,64,.07);display:flex;flex-direction:column;align-items:center;padding-top:18px}
.pillar .icon{width:74px;height:74px;border-radius:50%;background:#f4f5f7;display:flex;align-items:center;justify-content:center}
.pillar span{margin-top:20px;font-family:"Poppins",sans-serif;font-weight:500;font-size:17px;color:var(--navy)}
.benefit-photo{left:358px;top:1297px;width:299px;height:427px;background:linear-gradient(180deg,#ffffff 0%,#e9ecef 55%,#dde1e5 100%)}
.benefits h2{left:710px;top:1250px;width:400px;font-size:40px;font-weight:700;line-height:1.2}
.benefits p.lead{left:710px;top:1434px;width:390px;font-size:14px;line-height:2}
.benefits .btn{left:710px;top:1528px;width:233px;height:56px}
.review{left:720px;top:1650px;width:380px}
.review .who{display:flex;align-items:center;gap:20px;font-family:"Poppins",sans-serif;font-weight:500;font-size:16px;color:var(--navy)}
.review .who i{display:block;width:34px;height:34px;border-radius:50%;background:linear-gradient(135deg,#6f9fc0,#c08a56)}
.review blockquote{margin:12px 0 0 10px;border-left:3px solid var(--navy);padding-left:20px;font-size:14px;line-height:2}

/* banner */
.banner{left:99px;top:1943px;width:1002px;height:297px;background:linear-gradient(100deg,var(--orange-dark) 0%,#fb6a09 60%,#fd7a1a 100%);overflow:hidden}
.banner h2{left:62px;top:80px;width:520px;font-size:28px;font-weight:600;line-height:1.3;color:var(--white)}
.banner p{left:62px;top:170px;width:470px;font-size:14px;line-height:2;color:#ffe3cf}
.banner .quote-btn{left:644px;top:118px;width:203px;height:57px;background:var(--white);color:var(--navy);display:flex;align-items:center;justify-content:center;font-family:"Poppins",sans-serif;font-weight:600;font-size:16px}

/* services */
.svc-head h2{left:99px;top:2430px;width:380px;font-size:40px;font-weight:700;line-height:1.2}
.tabs{left:661px;top:2444px;display:flex;gap:30px;font-family:"Poppins",sans-serif;font-size:14px;font-weight:500;color:#b8c0c8}
.tabs .active{color:var(--navy);font-weight:600;padding:0 14px 10px;border-bottom:3px solid var(--orange)}
.svc-head p{left:661px;top:2494px;width:440px;font-size:14px;line-height:2}
.svc{width:334px;height:267px;padding:42px 0 0 44px}
.svc .icon{width:58px;height:58px;border-radius:50%;background:#f4f5f7;display:flex;align-items:center;justify-content:center}
.svc h3{margin-top:36px;font-size:24px;font-weight:500}
.svc p{margin-top:12px;width:230px;font-size:14px;line-height:2}
.vline{width:1px;background:var(--line)}
.hline{height:1px;background:var(--line)}

/* testimonial */
.testimonial-photo{left:99px;top:3443px;width:405px;height:492px;background:linear-gradient(180deg,#f1f1f1 0%,#f1f1f1 65%,var(--orange) 65%,var(--orange) 100%)}
.testimonial-photo::after{content:"";position:absolute;left:70px;top:30px;width:265px;height:462px;background:linear-gradient(180deg,#d9d7d5 0%,#8e949b 45%,#4a4f56 100%);border-radius:130px 130px 0 0;opacity:.85}
.quote blockquote{left:609px;top:3550px;width:496px;font-family:"Poppins",sans-serif;font-size:23px;font-weight:500;line-height:1.6;color:var(--navy)}
.quote .name{left:609px;top:3826px;font-family:"Poppins",sans-serif;font-size:17px;color:var(--navy)}
.quote .role{left:609px;top:3866px;font-family:"Poppins",sans-serif;font-size:17px;font-weight:600;color:var(--navy)}

/* footer */
.footer-brand{left:99px;top:4148px;display:flex;align-items:center;gap:12px;font-family:"Poppins",sans-serif;font-weight:600;font-size:22px;color:var(--navy)}
.footer-brand i{display:block;width:26px;height:26px;background:var(--navy);border-radius:5px}
.follow{left:99px;top:4196px;font-family:"Poppins",sans-serif;font-weight:600;font-size:16px;color:var(--navy)}
.socials{left:99px;top:4246px;display:flex;gap:16px}
.socials i{display:block;width:36px;height:36px;border-radius:50%;background:#eceef1}
.fcol{top:4146px;width:190px}
.fcol h4{font-size:17px;font-weight:500}
.fcol ul{list-style:none;margin-top:10px;font-size:13px;line-height:2}
.fcol li{display:flex;align-items:center;gap:8px}
.fcol li svg{flex:none}
.fbase{left:99px;top:4336px;width:1002px;height:1px;background:var(--line)}
.copy{left:99px;top:4356px;font-size:12px}
.to-top{left:1138px;top:4336px;width:36px;height:36px;border-radius:50%;background:var(--white);box-shadow:0 4px 14px rgba(0,0,0,.1);display:flex;align-items:center;justify-content:center}
</style>
</head>
<body>

<!-- Hero -->
<section class="hero abs">
  <div class="hero-glow abs"></div>
  <nav class="nav abs">
    <div class="nav-links"><span>Home</span><span>Services</span><span>About me</span><span>Contact</span></div>
    <div class="brand"><i></i>HK STEUERBERATUNG</div>
    <div class="nav-contact"><span>◍ +1-202-555-0147</span><span>✉ kontakt@hk-beispiel.de</span></div>
  </nav>
  <h1 class="abs">Willkommen<br>bei HK-<br>Steuerberatung!</h1>
  <p class="hero-lead abs">Ihrem Spezialisten bei allen steuerlichen Themen rund um Einkünfte &amp; Vermögen aus Krypto-Assets.</p>
  <a class="btn">Learn More</a>
  <div class="stats abs">
    <div class="stat"><b>30+</b><span>Years of<br>Excellence</span></div>
    <div class="stat"><b>53K</b><span>Completed<br>Policies</span></div>
    <div class="stat"><b>100%</b><span>Client<br>Satisfaction</span></div>
  </div>
  <div class="hero-photo abs" role="img" aria-label="Foto: jubelnder Geschäftsmann im grauen Anzug mit Laptop"></div>
  <div class="stat-card abs">
    <div class="row"><span>Month Stats</span><span>2019</span></div>
    <div class="row vals"><em>+2.4%</em><span>$648</span></div>
    <div class="bar"><i></i></div>
  </div>
  <div class="side-tools abs"><i></i><i></i><i></i><i></i><i></i></div>
</section>

<!-- Feature cards -->
<article class="feature abs" style="left:99px"><div class="num">01</div><h3>Consumer<br>Insights</h3><p>Duis aute irure dolor in reprehenderit voluptate velit esse cillum dolore eu fugiat nulla pariatur.</p></article>
<article class="feature abs" style="left:439px"><div class="num">02</div><h3>Emerging<br>Ideas</h3><p>In egestas erat imperdiet sed euismod nisi porta lorem mollis. At lectus urna duis.</p></article>
<article class="feature abs" style="left:778px"><div class="num">03</div><h3>Thought<br>Leadership</h3><p>Tincidunt nunc pulvinar sapien et ligula ullamcorper malesuada proin libero.</p></article>

<!-- Benefits -->
<section class="benefits">
  <div class="pillar abs" style="top:1263px"><div class="icon"><svg width="34" height="34" viewBox="0 0 34 34"><circle cx="22" cy="12" r="7" fill="none" stroke="#0f2540" stroke-width="3"/><circle cx="22" cy="12" r="2.5" fill="#0f2540"/><path d="M5 20l8 4-8 4z" fill="#f96a0b"/></svg></div><span>Vision</span></div>
  <div class="pillar abs" style="top:1442px"><div class="icon"><svg width="34" height="34" viewBox="0 0 34 34"><rect x="6" y="22" width="4" height="6" fill="#f96a0b"/><rect x="12" y="18" width="4" height="10" fill="#0f2540"/><rect x="18" y="14" width="4" height="14" fill="#0f2540"/><rect x="24" y="8" width="4" height="20" fill="#0f2540"/></svg></div><span>Missions</span></div>
  <div class="pillar abs" style="top:1625px"><div class="icon"><svg width="40" height="34" viewBox="0 0 40 34"><path d="M2 30l14-18 8 10 4-5 10 13z" fill="#0f2540"/><path d="M10 30l10-13 12 13z" fill="#f96a0b"/><path d="M16 12V2h8l-3 3 3 3h-8" fill="#f96a0b"/></svg></div><span>Goals</span></div>
  <div class="benefit-photo abs" role="img" aria-label="Foto: nachdenklicher Mann im weißen Hemd"></div>
  <h2 class="abs">Benefits of wellbeing and positive employee</h2>
  <p class="lead abs">Diam vulputate ut pharetra sit amet aliquam. Rhoncus est pellentesque elit ullamcorper.</p>
  <a class="btn">Meet our Team</a>
  <div class="review abs">
    <div class="who"><i role="img" aria-label="Profilbild"></i>Marek Holt</div>
    <blockquote>Kontor is awesome! Kontor has completely surpassed our expectations. After using Kontor my business skyrocketed!</blockquote>
  </div>
</section>

<!-- Banner -->
<section class="banner abs">
  <h2 class="abs">High quality services &amp; innovative solutions for reliable growth.</h2>
  <p class="abs">Rhoncus est pellentesque elit ullamcorper dignissim cras tincidunt lobortis feugiat. Sem et tortor consequat id porta.</p>
  <a class="quote-btn abs">Get a Quote</a>
</section>

<!-- Services -->
<section class="svc-head">
  <h2 class="abs">Service that lead the way to better business</h2>
  <div class="tabs abs"><span class="active">ABOUT US</span><span>MISSION</span><span>VISION</span></div>
  <p class="abs">Habitant morbi tristique senectus et netus et malesuada. Eget gravida cum sociis natoque penatibus et magnis dis. Adipiscing elit pellentesque habitant morbi. Sunt in culpa qui officia deserunt mollit anim id est laborum.</p>
</section>

<div class="vline abs" style="left:432px;top:2714px;height:535px"></div>
<div class="vline abs" style="left:766px;top:2714px;height:535px"></div>
<div class="hline abs" style="left:99px;top:2981px;width:1002px"></div>

<article class="svc abs" style="left:99px;top:2714px"><div class="icon"><svg width="22" height="22" viewBox="0 0 22 22"><path d="M5 5l12 12M17 5L5 17" stroke="#0f2540" stroke-width="2.5"/><circle cx="17" cy="5" r="2.5" fill="#f96a0b"/></svg></div><h3>Business Services</h3><p>Natoque penatibus et magnis dis parturient.</p></article>
<article class="svc abs" style="left:432px;top:2714px"><div class="icon"><svg width="24" height="24" viewBox="0 0 24 24"><rect x="7" y="7" width="10" height="10" rx="1" fill="#0f2540"/><path d="M12 1v4M12 19v4M1 12h4M19 12h4" stroke="#f96a0b" stroke-width="2.5"/></svg></div><h3>Consumer Product</h3><p>Sed vulputate mi sit amet mauris commodo quis imperdiet.</p></article>
<article class="svc abs" style="left:766px;top:2714px"><div class="icon"><svg width="24" height="24" viewBox="0 0 24 24"><circle cx="12" cy="12" r="7" fill="#0f2540"/><path d="M3 12a9 9 0 0 1 9-9" fill="none" stroke="#f96a0b" stroke-width="2"/><text x="12" y="15.5" text-anchor="middle" font-size="9" fill="#fff" font-family="Poppins,sans-serif">$</text></svg></div><h3>Financial Services</h3><p>Aliquam nulla facilisi cras fermentum odio eu.</p></article>
<article class="svc abs" style="left:99px;top:2981px"><div class="icon"><svg width="30" height="30" viewBox="0 0 30 30"><circle cx="10" cy="18" r="6" fill="#f96a0b"/><circle cx="10" cy="18" r="2" fill="#fff"/><circle cx="21" cy="9" r="4" fill="none" stroke="#0f2540" stroke-width="2.5"/></svg></div><h3>Treavel &amp; Aviation</h3><p>Cum sociis natoque penatibus et magnis dis dignissim cras tincidunt.</p></article>
<article class="svc abs" style="left:432px;top:2981px"><div class="icon"><svg width="24" height="24" viewBox="0 0 24 24"><rect x="3" y="5" width="18" height="14" rx="2" fill="#0f2540"/><path d="M10 10l-2 2 2 2M14 10l2 2-2 2" stroke="#f96a0b" stroke-width="1.5" fill="none"/></svg></div><h3>Software Research</h3><p>Cras sed felis eget velit aliquet sagittis id consectetur purus.</p></article>
<article class="svc abs" style="left:766px;top:2981px"><div class="icon"><svg width="26" height="26" viewBox="0 0 26 26"><path d="M4 9h18l-9 13z" fill="#0f2540"/><path d="M8 9l5 13 5-13" fill="#f96a0b"/><path d="M13 1v4M4 4l2 2M22 4l-2 2" stroke="#f96a0b" stroke-width="2"/></svg></div><h3>Quality Resourcing</h3><p>Imperdiet nulla malesuada pellent esque elit eget gravida.</p></article>

<!-- Testimonial -->
<div class="testimonial-photo abs" role="img" aria-label="Foto: lächelnder Handwerker im grauen Overall mit Werkzeuggürtel"></div>
<section class="quote">
  <svg class="abs" style="left:609px;top:3491px" width="44" height="36" viewBox="0 0 44 36"><path d="M0 36V18C0 8 5 2 16 0v7c-5 1-7 4-7 9h7v20zM24 36V18c0-10 5-16 16-18v7c-5 1-7 4-7 9h7v20z" fill="#f96a0b"/></svg>
  <blockquote class="abs">"I couldn't have asked for more than this. I will refer everyone I know. I like Kontor more and more each day because it makes my life a lot easier. It really saves me time and effort. Kontor is exactly what our business has been lacking."</blockquote>
  <div class="name abs">Lorenz Abel</div>
  <div class="role abs">CEO nordwerk.de</div>
</section>

<!-- Footer -->
<footer>
  <div class="footer-brand abs"><i></i>Kontor</div>
  <div class="follow abs">Follow us:</div>
  <div class="socials abs"><i></i><i></i><i></i><i></i></div>
  <div class="fcol abs" style="left:311px"><h4>Company</h4><ul><li>Global Locations</li><li>Mission</li><li>Careers</li></ul></div>
  <div class="fcol abs" style="left:513px"><h4>Resources</h4><ul><li>Services</li><li>Clients</li><li>Contact</li></ul></div>
  <div class="fcol abs" style="left:714px"><h4>Legal</h4><ul><li>Privacy Policy</li><li>Terms &amp; Conditions</li></ul></div>
  <div class="fcol abs" style="left:916px"><h4>Contact us</h4><ul>
    <li><svg width="12" height="12" viewBox="0 0 12 12"><path d="M2 1h3l1 3-2 1a7 7 0 0 0 3 3l1-2 3 1v3c-6 0-9-3-9-9z" fill="none" stroke="#5b6470"/></svg>+1-202-555-0147</li>
    <li><svg width="12" height="12" viewBox="0 0 12 12"><rect x="1" y="2.5" width="10" height="7" fill="none" stroke="#5b6470"/><path d="M1 3l5 4 5-4" fill="none" stroke="#5b6470"/></svg>hallo@hk-beispiel.de</li>
    <li><svg width="12" height="12" viewBox="0 0 12 12"><circle cx="6" cy="4" r="2.5" fill="none" stroke="#5b6470"/><path d="M1 11c1-3 9-3 10 0" fill="none" stroke="#5b6470"/></svg>18 Lindenweg, Haus 4</li>
  </ul></div>
  <div class="fbase abs"></div>
  <div class="copy abs">© 2022 Your Company . All Rights Reserved.</div>
  <div class="to-top abs"><svg width="10" height="6" viewBox="0 0 10 6"><path d="M1 5l4-4 4 4" fill="none" stroke="#0f2540" stroke-width="1.5"/></svg></div>
</footer>

</body>
</html>
```